Author of book needs a Facebook page to route possible customers to the books website.

I need a Facebook page to promote my new book: Keeping Watch Alone-A Daily Safety Handbook For Ladies-Revisited. Idealy the Facebook page must include a picture of the book, an author bio and a short paragraph or two about the book. All of this can be obtained at the books website at www.trailguardnotes.com. Since I am expecting a high volume of visitors I need the Facebook page to be "Liked" rather than "Friends."

Target Market(s)

Women of all ages

Font styles to use
Sans Serif

Colors

Designer to choose colors to be used in the design.

Requirements
Must have
• Link to the www.trailguardnotes.com website. Picture of the book cover. Author bio.

```html
<!DOCTYPE html>
<html lang="en">
<head>
<meta charset="utf-8">
<title>Keeping Watch Alone – Facebook Cover</title>
<link rel="stylesheet" href="https://fonts.googleapis.com/css2?family=Open+Sans:wght@300;400;600;700;800&family=Roboto+Slab:wght@700&family=Kaushan+Script&display=swap">
<style>
  :root {
    --paper: #f4f4f4;
    --photo-light: #ececec;
    --photo-mid: #d4d4d4;
    --photo-dark: #a4a4a4;
    --ink: #1f1f1f;
    --ink-soft: #4a4a4a;
    --ink-muted: #6b6b6b;
    --accent: #f08a1e;
    --cover-black: #121212;
    --cover-spine: #2c2c2c;
    --cover-text: #f2f2f2;
    --art-dark: #2a2a2a;
    --art-light: #5a5a5a;
  }
  * { margin: 0; padding: 0; box-sizing: border-box; }
  html, body { width: 1200px; height: 458px; overflow: hidden; background: var(--paper); }
  .cover {
    position: relative;
    width: 1200px;
    height: 458px;
    overflow: hidden;
    background: var(--paper);
    font-family: "Open Sans", Arial, sans-serif;
  }
  .backdrop-photo {
    position: absolute;
    inset: 0;
    background:
      linear-gradient(90deg, var(--paper) 0%, var(--paper) 30%, rgba(244,244,244,0.45) 60%, rgba(244,244,244,0) 100%),
      linear-gradient(180deg, var(--photo-light) 0%, var(--photo-mid) 55%, var(--photo-dark) 100%);
  }

  /* book */
  .book {
    position: absolute;
    left: 50px;
    top: 20px;
    width: 276px;
    height: 414px;
    z-index: 3;
    filter: drop-shadow(8px 10px 14px rgba(0,0,0,0.35));
  }
  .book-spine {
    position: absolute;
    left: 0;
    top: 8px;
    width: 20px;
    height: 400px;
    background: linear-gradient(90deg, #1a1a1a 0%, var(--cover-spine) 60%, #0c0c0c 100%);
  }
  .book-face {
    position: absolute;
    left: 18px;
    top: 0;
    width: 258px;
    height: 414px;
    background: var(--cover-black);
    color: var(--cover-text);
    text-align: center;
    font-weight: 300;
  }
  .book-edition {
    position: absolute;
    top: 44px;
    left: 0;
    width: 100%;
    font-size: 9.5px;
    letter-spacing: 1px;
    font-weight: 400;
  }
  .book-title-top {
    position: absolute;
    top: 60px;
    left: 0;
    width: 100%;
    font-size: 25px;
    line-height: 30px;
  }
  .book-title-main {
    position: absolute;
    top: 88px;
    left: 0;
    width: 100%;
    font-size: 44px;
    line-height: 50px;
  }
  .book-art {
    position: absolute;
    top: 148px;
    left: 34px;
    width: 190px;
    height: 172px;
    background: radial-gradient(circle at 45% 45%, var(--art-light) 0%, var(--art-dark) 70%, var(--cover-black) 100%);
  }
  .book-subtitle {
    position: absolute;
    top: 330px;
    left: 0;
    width: 100%;
    font-size: 13px;
    line-height: 17px;
    font-weight: 400;
  }
  .book-subtitle .book-mark {
    font-family: "Kaushan Script", cursive;
    color: var(--accent);
    font-size: 12px;
    margin-left: 3px;
  }
  .book-author {
    position: absolute;
    top: 378px;
    left: 0;
    width: 100%;
    font-size: 16px;
    letter-spacing: 3px;
    font-weight: 400;
  }

  /* text column */
  .author-name {
    position: absolute;
    left: 416px;
    top: 14px;
    font-size: 34px;
    font-weight: 800;
    letter-spacing: 0.5px;
    color: var(--ink);
  }
  .author-rule {
    position: absolute;
    left: 416px;
    top: 68px;
    width: 170px;
    height: 3px;
    background: var(--accent);
  }
  .book-title {
    position: absolute;
    left: 416px;
    top: 84px;
    font-size: 47px;
    line-height: 52px;
    font-weight: 700;
    color: var(--ink);
    letter-spacing: -0.5px;
  }
  .book-tagline {
    position: absolute;
    left: 416px;
    top: 198px;
    font-size: 28px;
    line-height: 34px;
    font-weight: 700;
    color: var(--ink-soft);
  }
  .edition-mark {
    font-family: "Kaushan Script", cursive;
    font-weight: 400;
    color: var(--accent);
    font-size: 32px;
    margin-left: 10px;
    position: relative;
    top: -4px;
  }
  .book-pitch {
    position: absolute;
    left: 416px;
    top: 280px;
    width: 500px;
    font-size: 20px;
    line-height: 25px;
    font-weight: 600;
    color: var(--ink-muted);
  }
  .link-band {
    position: absolute;
    left: 0;
    top: 385px;
    width: 1200px;
    height: 44px;
    background: var(--accent);
    z-index: 2;
  }
  .site-link {
    position: absolute;
    left: 456px;
    top: 0;
    height: 44px;
    line-height: 44px;
    font-family: "Roboto Slab", Georgia, serif;
    font-weight: 700;
    font-size: 26px;
    color: var(--ink);
  }
</style>
</head>
<body>
  <main class="cover">
    <div class="backdrop-photo" role="img" aria-label="Faded photograph of a woman walking alone followed by a hooded figure in an alley"></div>

    <div class="book">
      <div class="book-spine"></div>
      <div class="book-face">
        <p class="book-edition">2017 REVISED UPDATED EDITION</p>
        <p class="book-title-top">KEEPING WATCH</p>
        <p class="book-title-main">ALONE</p>
        <div class="book-art" role="img" aria-label="Black and white illustration of a woman holding a knife"></div>
        <p class="book-subtitle">A DAILY SAFETY HANDBOOK<br>FOR LADIES<span class="book-mark">Revisited</span></p>
        <p class="book-author">DANIEL MARSH</p>
      </div>
    </div>

    <h2 class="author-name">DANIEL MARSH</h2>
    <div class="author-rule"></div>

    <h1 class="book-title">Keeping<br>Watch Alone</h1>

    <p class="book-tagline">A Daily Safety Handbook<br>For Ladies<span class="edition-mark">Revisited</span></p>

    <p class="book-pitch">The Practical Guide for deterring Rapists, Stalkers, Serial Killers, Hit Men, Terrorists and other assorted criminals.</p>

    <div class="link-band">
      <span class="site-link">http://www.trailguardnotes.com/</span>
    </div>
  </main>
</body>
</html>
```